Pitch Deck and business cards for Virtual Reality Startup

We need a redesign of our pitch deck to be funky, creative and interactive with animated graphics inline with our product (VR training)
Note: the design does not have to be orange that's just a template of the information we're sending you so we would like to see other colours also.

Target Market(s)

Investors

Industry/Entity Type

Media

Contact Information for Business Card

logo, Name, title, address, telephone, email, website

Font styles to use
Other font styles liked:
• funky but readable

Colors

Designer to choose colors to be used in the design.

Requirements
Must have
• Exciting non traditional design that fits a new, innovative, exciting and interactive technology
Nice to have
• .
Should not have
• traditional look and feel.

```html
<!DOCTYPE html>
<html lang="en">
<head>
<meta charset="utf-8">
<title>LUMA XR — Pitch Deck Colourways</title>
<link href="https://fonts.googleapis.com/css2?family=Roboto:wght@400;500;700;900&display=swap" rel="stylesheet">
<style>
:root{--bg:#e8e8e8;--ink:#111;--white:#fff;--grey:#8a8a8a}
.theme-blue{--c1:#10b2ef;--c2:#1c5cc0;--hl:#2aa8ea;--bar1:#1677cf;--bar2:#1a8ade;--ring:#29a3e8;--s1:#111;--s2:#1b9be0;--s3:#3a6fc9;--fund:#2f8fe0;--photo:#2b6aa8}
.theme-purple{--c1:#1f8ef0;--c2:#7b3aad;--hl:#2b8cf0;--bar1:#7b3fb0;--bar2:#6a3fb5;--ring:#7b3fb0;--s1:#111;--s2:#2a86ee;--s3:#6e3aa8;--fund:#6e44c0;--photo:#4f58b8}
.theme-green{--c1:#3fc56e;--c2:#f5b31a;--hl:#4cc46a;--bar1:#f2b21e;--bar2:#49c36c;--ring:#f2b21e;--s1:#2a3347;--s2:#f2b21e;--s3:#3fbf6a;--fund:#c9c028;--photo:#8fb84a}
*{margin:0;padding:0;box-sizing:border-box}
html,body{width:1200px;height:570px;overflow:hidden}
body{background:var(--bg);font-family:"Roboto",Arial,sans-serif;position:relative}
.deck{position:absolute;top:7px;display:grid;grid-template-columns:186px 186px;grid-auto-rows:104.5px;column-gap:5.5px;row-gap:5px}
.deck-1{left:7.5px}.deck-2{left:411px}.deck-3{left:815px}
.slide{position:relative;overflow:hidden;background:var(--white);box-shadow:0 2px 4px rgba(0,0,0,.35);border-bottom:2px solid var(--c2)}
.grad{background:linear-gradient(155deg,var(--c1),var(--c2))}
.layer{position:absolute;inset:0;width:100%;height:100%}
.mark{position:absolute;top:4px;right:5px;font-size:4.2px;font-weight:900;color:var(--ink);letter-spacing:.2px}
.photo{position:absolute}
/* title */
.title-mark{position:absolute;left:7px;top:17px;font-size:14px;font-weight:900;color:var(--ink);letter-spacing:.5px}
.title-text{position:absolute;left:6px;top:40px;color:#fff;font-weight:700;font-size:12.5px;line-height:13.5px}
.badge{position:absolute;left:3px;bottom:3px;width:11px;height:11px;background:#ddd;border:1px solid #fff}
/* story */
.story-title{position:absolute;top:6px;width:100%;text-align:center;color:#fff;font-weight:700;font-size:19px}
.clip{position:absolute;left:56px;top:40px;width:74px;height:64px;background:#fff;box-shadow:0 0 2px rgba(0,0,0,.4);padding:2px 3px}
.clip-head{font-size:3px;line-height:3.3px;font-weight:700;color:#222}
.clip-by{font-size:1.8px;color:#777;margin:1px 0}
.clip-photo{height:46px;background:linear-gradient(160deg,#6d8a5a,#3a4a3a)}
/* problem */
.problem-label{position:absolute;left:12px;top:52px;color:var(--hl);font-weight:700;font-size:8.5px;line-height:9.5px;text-align:center}
.problem-copy{position:absolute;left:104px;top:20px;width:78px;text-align:center;color:#fff;font-weight:500;font-size:8px;line-height:9px}
.job-ready{position:absolute;left:104px;top:66px;width:82px;text-align:center;color:#fff;font-weight:700;font-size:13.5px}
/* traditional */
.trad-text{position:absolute;left:112px;top:38px;width:72px;text-align:center;font-weight:700;font-size:12.5px;line-height:13.5px;color:var(--ink)}
/* vr */
.vr-text{position:absolute;left:12px;top:30px;font-weight:700;font-size:11.5px;line-height:13.5px;color:var(--ink)}
.ticks{position:absolute;left:90px;top:18px;list-style:none;color:#fff;font-size:6px;font-weight:500}
.ticks li{display:flex;align-items:center;gap:2px;margin-bottom:7px}
.ticks svg{width:6px;height:6px}
/* team */
.uniq-strip{position:absolute;left:0;top:0;width:28px;height:100%;background:#fff}
.uniq-text{position:absolute;left:14px;top:50%;transform:translate(-50%,-50%) rotate(-90deg);white-space:nowrap;font-weight:500;font-size:9px;color:var(--ink)}
.band{position:absolute;left:28px;right:0;height:23px;background:#0c0c0c}
.band-a{top:27px}.band-b{top:70px}
.member{position:absolute;width:52px;text-align:center;color:#fff}
.avatar{width:16px;height:16px;border-radius:50%;background:#cfd6de;border:1.5px solid #fff;margin:0 auto 1px}
.m-name{font-size:2.6px;font-weight:700}
.m-role{font-size:1.9px;line-height:2.2px}
/* process */
.process-title{position:absolute;left:8px;top:16px;color:#fff;font-weight:700;font-size:14px;line-height:15px;text-align:center}
.seg-label{font-size:2.6px;fill:#fff;font-weight:500;text-anchor:middle}
/* business */
.bm-title{position:absolute;top:8px;width:100%;text-align:center;font-weight:700;font-size:13.5px;color:var(--ink)}
.bar{position:absolute;height:26px;color:#fff;font-weight:500;font-size:8px;line-height:9px;display:flex;align-items:center}
.bar-1{left:0;top:33px;width:148px;background:var(--bar1);border-radius:0 13px 13px 0;padding-left:26px}
.bar-2{right:0;top:64px;width:148px;background:var(--bar2);border-radius:13px 0 0 13px;padding-left:28px;text-align:center}
.bar-icon{position:absolute;width:22px;height:22px;border-radius:50%;background:var(--ink);border:1.5px solid #fff;color:#fff;display:flex;align-items:center;justify-content:center;font-size:8px;font-weight:700}
.bar-1 .bar-icon{right:2px;top:2px}.bar-2 .bar-icon{left:2px;top:2px}
/* ask */
.ask-label{position:absolute;left:30px;top:41px;width:36px;text-align:center;font-weight:700;font-size:9.5px;line-height:10px;color:var(--ink)}
.pill{position:absolute;left:104px;width:68px;height:14px;border-radius:7px;color:#fff;font-size:5.5px;font-weight:700;display:flex;align-items:center;padding-left:25px}
.pill-intro{top:7px;background:var(--ink)}.pill-fund{top:43px;background:var(--fund)}.pill-inv{top:78px;background:#7e7e7e}
.pill-icon{position:absolute;left:-3px;top:-2px;width:18px;height:18px;border-radius:50%;background:var(--ink);border:1.2px solid #fff;display:flex;align-items:center;justify-content:center;font-size:7px}
.pill-fund .pill-icon{background:var(--fund)}.pill-inv .pill-icon{background:#7e7e7e}
/* questions */
.q-text{position:absolute;top:28px;width:100%;text-align:center;color:#fff;font-weight:700;font-size:22px;line-height:24px}
</style>
</head>
<body>

<!-- deck template repeated per colourway -->
<section class="deck deck-1 theme-blue" aria-label="Deck in blue">
  <div class="slide grad">
    <div class="photo layer" style="left:96px;width:90px;background:linear-gradient(90deg,rgba(0,0,0,0),rgba(10,20,40,.45))" role="img" aria-label="Photo of a man wearing a VR headset"></div>
    <div class="title-mark">LUMA XR</div>
    <h1 class="title-text">THE FUTURE OF<br>HOSPITALITY<br>TRAINING</h1>
    <div class="badge"></div>
  </div>
  <div class="slide grad">
    <svg class="layer" viewBox="0 0 186 104" preserveAspectRatio="none"><path d="M0 104V88C40 72 70 98 110 78C150 60 158 32 186 40V104Z" fill="#fff"/></svg>
    <div class="mark">LUMA XR</div>
    <h2 class="story-title">Anna’s story…</h2>
    <div class="clip" role="img" aria-label="Newspaper clipping with photo of two men">
      <div class="clip-head">Trainee’s case reviewed after late-night venue incident in Port Ellis</div>
      <div class="clip-by">By staff reporter · updated today</div>
      <div class="clip-photo"></div>
    </div>
  </div>
  <div class="slide grad">
    <svg class="layer" viewBox="0 0 186 104" preserveAspectRatio="none" role="img" aria-label="Photo of a man in a suit"><path d="M0 0H112C96 20 70 30 76 55C82 80 60 94 70 104H0Z" fill="#222"/></svg>
    <div class="mark">LUMA XR</div>
    <div class="problem-label">THE<br>PROBLEM</div>
    <p class="problem-copy">Traditional training does not prepare staff to be</p>
    <p class="job-ready">Job Ready</p>
  </div>
  <div class="slide">
    <div class="layer grad" style="opacity:.6" role="img" aria-label="Photo of a bored student resting on a desk"></div>
    <svg class="layer" viewBox="0 0 186 104" preserveAspectRatio="none"><path d="M186 0H104C126 16 106 40 114 56C122 76 150 86 160 104H186Z" fill="#fff"/></svg>
    <p class="trad-text">Traditional training</p>
  </div>
  <div class="slide grad">
    <svg class="layer" viewBox="0 0 186 104" preserveAspectRatio="none"><path d="M0 0H96C80 16 96 36 86 56C76 76 86 94 80 104H0Z" fill="#fff"/></svg>
    <div class="mark">LUMA XR</div>
    <p class="vr-text">Virtual<br>reality<br>training</p>
    <ul class="ticks">
      <li><svg viewBox="0 0 10 10"><circle cx="5" cy="5" r="5" fill="#fff"/><path d="M2.5 5l1.8 1.8L7.6 3.4" stroke="var(--c2)" stroke-width="1.4" fill="none"/></svg>Retention of knowledge</li>
      <li><svg viewBox="0 0 10 10"><circle cx="5" cy="5" r="5" fill="#fff"/><path d="M2.5 5l1.8 1.8L7.6 3.4" stroke="var(--c2)" stroke-width="1.4" fill="none"/></svg>Real-life experiences</li>
      <li><svg viewBox="0 0 10 10"><circle cx="5" cy="5" r="5" fill="#fff"/><path d="M2.5 5l1.8 1.8L7.6 3.4" stroke="var(--c2)" stroke-width="1.4" fill="none"/></svg>Immersive &amp; engaging</li>
    </ul>
    <div class="photo" style="left:80px;top:56px;width:92px;height:48px;background:linear-gradient(90deg,rgba(20,20,30,.55),rgba(230,230,230,.55));border-radius:20px 20px 0 0" role="img" aria-label="Two people wearing VR headsets"></div>
  </div>
  <div class="slide grad">
    <div class="uniq-strip"><span class="uniq-text">What makes us unique?</span></div>
    <div class="mark">LUMA XR</div>
    <div class="band band-a"></div><div class="band band-b"></div>
    <div class="member" style="left:36px;top:19px"><div class="avatar"></div><div class="m-name">OWEN HALE</div><div class="m-role">Co Founder and CEO</div></div>
    <div class="member" style="left:84px;top:19px"><div class="avatar"></div><div class="m-name">DR LENA MARSH</div><div class="m-role">Learning and Development Strategist</div></div>
    <div class="member" style="left:132px;top:19px"><div class="avatar"></div><div class="m-name">RITA OKAFOR</div><div class="m-role">Co Founder, Education and Content Director</div></div>
    <div class="member" style="left:36px;top:62px"><div class="avatar"></div><div class="m-name">FELIX BRANDT</div><div class="m-role">360 Film and Post-Production Expert</div></div>
    <div class="member" style="left:84px;top:62px"><div class="avatar"></div><div class="m-name">NORA QUILL</div><div class="m-role">Learning Designer</div></div>
    <div class="member" style="left:132px;top:62px"><div class="avatar"></div><div class="m-name">KEN ARATA</div><div class="m-role">Programmer and Game Developer</div></div>
  </div>
  <div class="slide grad">
    <svg class="layer" viewBox="0 0 186 104" preserveAspectRatio="none"><path d="M82 0H186V104H0V86C20 96 30 72 46 70C64 68 70 50 74 40C80 24 70 14 82 0Z" fill="#fff"/></svg>
    <div class="mark">LUMA XR</div>
    <p class="process-title">Our<br>Process</p>
    <svg class="layer" viewBox="0 0 186 104">
      <g transform="rotate(-112 138 53)" fill="none" stroke-width="15">
        <circle cx="138" cy="53" r="38" style="stroke:var(--s1)" stroke-dasharray="28.8 269.8"/>
        <circle cx="138" cy="53" r="38" style="stroke:var(--s2)" stroke-dasharray="0 29.8 28.8 240"/>
        <circle cx="138" cy="53" r="38" style="stroke:var(--s2)" stroke-dasharray="0 59.6 28.8 210"/>
        <circle cx="138" cy="53" r="38" style="stroke:var(--s1)" stroke-dasharray="0 89.4 28.8 180"/>
        <circle cx="138" cy="53" r="38" style="stroke:var(--s3)" stroke-dasharray="0 119.2 28.8 150"/>
        <circle cx="138" cy="53" r="38" style="stroke:var(--s1)" stroke-dasharray="0 149 28.8 120"/>
        <circle cx="138" cy="53" r="38" style="stroke:var(--s3)" stroke-dasharray="0 178.8 28.8 90"/>
        <circle cx="138" cy="53" r="38" style="stroke:var(--s1)" stroke-dasharray="0 208.6 28.8 60"/>
      </g>
      <text class="seg-label" x="125" y="17">Release</text>
      <text class="seg-label" x="151" y="17">Research</text><text class="seg-label" x="151" y="20">topics</text>
      <text class="seg-label" x="172" y="38">Create</text><text class="seg-label" x="172" y="41">Content</text>
      <text class="seg-label" x="171" y="70">Learning</text><text class="seg-label" x="171" y="73">Design</text>
      <text class="seg-label" x="151" y="88">360 Film</text><text class="seg-label" x="151" y="91">Production</text>
      <text class="seg-label" x="123" y="88">360 Post</text><text class="seg-label" x="123" y="91">Production</text>
      <text class="seg-label" x="104" y="67">Interactive</text><text class="seg-label" x="104" y="70">Gaming</text><text class="seg-label" x="104" y="73">Development</text>
      <text class="seg-label" x="104" y="37">Testing</text>
    </svg>
  </div>
  <div class="slide">
    <div class="mark">LUMA XR</div>
    <h2 class="bm-title">Business model</h2>
    <div class="bar bar-1">Partnerships with<br>training providers<span class="bar-icon">&#9679;&#9679;</span></div>
    <div class="bar bar-2"><span class="bar-icon">$</span>Subscription based with new content released monthly</div>
  </div>
  <div class="slide">
    <div class="mark">LUMA XR</div>
    <svg class="layer" viewBox="0 0 186 104">
      <path d="M48 22C70 22 84 14 100 14M66 52H100M48 82C70 82 84 85 100 85" stroke="#111" stroke-width="1.6" fill="none"/>
      <circle cx="48" cy="52" r="30" fill="none" stroke="#111" stroke-width="3"/>
      <circle cx="48" cy="52" r="24" fill="none" style="stroke:var(--ring)" stroke-width="3.5"/>
      <circle cx="48" cy="52" r="18" fill="#fff" stroke="#888" stroke-width="2.5"/>
    </svg>
    <p class="ask-label">Our<br>ask</p>
    <div class="pill pill-intro"><span class="pill-icon">&#10070;</span>Introductions</div>
    <div class="pill pill-fund"><span class="pill-icon">$</span>Funding</div>
    <div class="pill pill-inv"><span class="pill-icon">&#9679;&#9679;</span>Investors</div>
  </div>
  <div class="slide grad">
    <div class="layer" style="background:linear-gradient(90deg,rgba(255,255,255,0),rgba(255,255,255,.18))" role="img" aria-label="Faint photo of a person wearing a VR headset"></div>
    <div class="mark">LUMA XR</div>
    <p class="q-text">Questions<br>?</p>
  </div>
</section>

<section class="deck deck-2 theme-purple" aria-label="Deck in blue and purple">
  <div class="slide grad">
    <div class="photo layer" style="left:96px;width:90px;background:linear-gradient(90deg,rgba(0,0,0,0),rgba(10,20,40,.45))" role="img" aria-label="Photo of a man wearing a VR headset"></div>
    <div class="title-mark">LUMA XR</div>
    <h1 class="title-text">THE FUTURE OF<br>HOSPITALITY<br>TRAINING</h1>
    <div class="badge"></div>
  </div>
  <div class="slide grad">
    <svg class="layer" viewBox="0 0 186 104" preserveAspectRatio="none"><path d="M0 104V88C40 72 70 98 110 78C150 60 158 32 186 40V104Z" fill="#fff"/></svg>
    <div class="mark">LUMA XR</div>
    <h2 class="story-title">Anna’s story…</h2>
    <div class="clip" role="img" aria-label="Newspaper clipping with photo of two men">
      <div class="clip-head">Trainee’s case reviewed after late-night venue incident in Port Ellis</div>
      <div class="clip-by">By staff reporter · updated today</div>
      <div class="clip-photo"></div>
    </div>
  </div>
  <div class="slide grad">
    <svg class="layer" viewBox="0 0 186 104" preserveAspectRatio="none" role="img" aria-label="Photo of a man in a suit"><path d="M0 0H112C96 20 70 30 76 55C82 80 60 94 70 104H0Z" fill="#222"/></svg>
    <div class="mark">LUMA XR</div>
    <div class="problem-label">THE<br>PROBLEM</div>
    <p class="problem-copy">Traditional training does not prepare staff to be</p>
    <p class="job-ready">Job Ready</p>
  </div>
  <div class="slide">
    <div class="layer grad" style="opacity:.6" role="img" aria-label="Photo of a bored student resting on a desk"></div>
    <svg class="layer" viewBox="0 0 186 104" preserveAspectRatio="none"><path d="M186 0H104C126 16 106 40 114 56C122 76 150 86 160 104H186Z" fill="#fff"/></svg>
    <p class="trad-text">Traditional training</p>
  </div>
  <div class="slide grad">
    <svg class="layer" viewBox="0 0 186 104" preserveAspectRatio="none"><path d="M0 0H96C80 16 96 36 86 56C76 76 86 94 80 104H0Z" fill="#fff"/></svg>
    <div class="mark">LUMA XR</div>
    <p class="vr-text">Virtual<br>reality<br>training</p>
    <ul class="ticks">
      <li><svg viewBox="0 0 10 10"><circle cx="5" cy="5" r="5" fill="#fff"/><path d="M2.5 5l1.8 1.8L7.6 3.4" stroke="var(--c2)" stroke-width="1.4" fill="none"/></svg>Retention of knowledge</li>
      <li><svg viewBox="0 0 10 10"><circle cx="5" cy="5" r="5" fill="#fff"/><path d="M2.5 5l1.8 1.8L7.6 3.4" stroke="var(--c2)" stroke-width="1.4" fill="none"/></svg>Real-life experiences</li>
      <li><svg viewBox="0 0 10 10"><circle cx="5" cy="5" r="5" fill="#fff"/><path d="M2.5 5l1.8 1.8L7.6 3.4" stroke="var(--c2)" stroke-width="1.4" fill="none"/></svg>Immersive &amp; engaging</li>
    </ul>
    <div class="photo" style="left:80px;top:56px;width:92px;height:48px;background:linear-gradient(90deg,rgba(20,20,30,.55),rgba(230,230,230,.55));border-radius:20px 20px 0 0" role="img" aria-label="Two people wearing VR headsets"></div>
  </div>
  <div class="slide grad">
    <div class="uniq-strip"><span class="uniq-text">What makes us unique?</span></div>
    <div class="mark">LUMA XR</div>
    <div class="band band-a"></div><div class="band band-b"></div>
    <div class="member" style="left:36px;top:19px"><div class="avatar"></div><div class="m-name">OWEN HALE</div><div class="m-role">Co Founder and CEO</div></div>
    <div class="member" style="left:84px;top:19px"><div class="avatar"></div><div class="m-name">DR LENA MARSH</div><div class="m-role">Learning and Development Strategist</div></div>
    <div class="member" style="left:132px;top:19px"><div class="avatar"></div><div class="m-name">RITA OKAFOR</div><div class="m-role">Co Founder, Education and Content Director</div></div>
    <div class="member" style="left:36px;top:62px"><div class="avatar"></div><div class="m-name">FELIX BRANDT</div><div class="m-role">360 Film and Post-Production Expert</div></div>
    <div class="member" style="left:84px;top:62px"><div class="avatar"></div><div class="m-name">NORA QUILL</div><div class="m-role">Learning Designer</div></div>
    <div class="member" style="left:132px;top:62px"><div class="avatar"></div><div class="m-name">KEN ARATA</div><div class="m-role">Programmer and Game Developer</div></div>
  </div>
  <div class="slide grad">
    <svg class="layer" viewBox="0 0 186 104" preserveAspectRatio="none"><path d="M82 0H186V104H0V86C20 96 30 72 46 70C64 68 70 50 74 40C80 24 70 14 82 0Z" fill="#fff"/></svg>
    <div class="mark">LUMA XR</div>
    <p class="process-title">Our<br>Process</p>
    <svg class="layer" viewBox="0 0 186 104">
      <g transform="rotate(-112 138 53)" fill="none" stroke-width="15">
        <circle cx="138" cy="53" r="38" style="stroke:var(--s1)" stroke-dasharray="28.8 269.8"/>
        <circle cx="138" cy="53" r="38" style="stroke:var(--s2)" stroke-dasharray="0 29.8 28.8 240"/>
        <circle cx="138" cy="53" r="38" style="stroke:var(--s3)" stroke-dasharray="0 59.6 28.8 210"/>
        <circle cx="138" cy="53" r="38" style="stroke:var(--s1)" stroke-dasharray="0 89.4 28.8 180"/>
        <circle cx="138" cy="53" r="38" style="stroke:var(--s2)" stroke-dasharray="0 119.2 28.8 150"/>
        <circle cx="138" cy="53" r="38" style="stroke:var(--s1)" stroke-dasharray="0 149 28.8 120"/>
        <circle cx="138" cy="53" r="38" style="stroke:var(--s3)" stroke-dasharray="0 178.8 28.8 90"/>
        <circle cx="138" cy="53" r="38" style="stroke:var(--s1)" stroke-dasharray="0 208.6 28.8 60"/>
      </g>
      <text class="seg-label" x="125" y="17">Release</text>
      <text class="seg-label" x="151" y="17">Research</text><text class="seg-label" x="151" y="20">topics</text>
      <text class="seg-label" x="172" y="38">Create</text><text class="seg-label" x="172" y="41">Content</text>
      <text class="seg-label" x="171" y="70">Learning</text><text class="seg-label" x="171" y="73">Design</text>
      <text class="seg-label" x="151" y="88">360 Film</text><text class="seg-label" x="151" y="91">Production</text>
      <text class="seg-label" x="123" y="88">360 Post</text><text class="seg-label" x="123" y="91">Production</text>
      <text class="seg-label" x="104" y="67">Interactive</text><text class="seg-label" x="104" y="70">Gaming</text><text class="seg-label" x="104" y="73">Development</text>
      <text class="seg-label" x="104" y="37">Testing</text>
    </svg>
  </div>
  <div class="slide">
    <div class="mark">LUMA XR</div>
    <h2 class="bm-title">Business model</h2>
    <div class="bar bar-1">Partnerships with<br>training providers<span class="bar-icon">&#9679;&#9679;</span></div>
    <div class="bar bar-2"><span class="bar-icon">$</span>Subscription based with new content released monthly</div>
  </div>
  <div class="slide">
    <div class="mark">LUMA XR</div>
    <svg class="layer" viewBox="0 0 186 104">
      <path d="M48 22C70 22 84 14 100 14M66 52H100M48 82C70 82 84 85 100 85" stroke="#111" stroke-width="1.6" fill="none"/>
      <circle cx="48" cy="52" r="30" fill="none" stroke="#111" stroke-width="3"/>
      <circle cx="48" cy="52" r="24" fill="none" style="stroke:var(--ring)" stroke-width="3.5"/>
      <circle cx="48" cy="52" r="18" fill="#fff" stroke="#888" stroke-width="2.5"/>
    </svg>
    <p class="ask-label">Our<br>ask</p>
    <div class="pill pill-intro"><span class="pill-icon">&#10070;</span>Introductions</div>
    <div class="pill pill-fund"><span class="pill-icon">$</span>Funding</div>
    <div class="pill pill-inv"><span class="pill-icon">&#9679;&#9679;</span>Investors</div>
  </div>
  <div class="slide grad">
    <div class="layer" style="background:linear-gradient(90deg,rgba(255,255,255,0),rgba(255,255,255,.18))" role="img" aria-label="Faint photo of a person wearing a VR headset"></div>
    <div class="mark">LUMA XR</div>
    <p class="q-text">Questions<br>?</p>
  </div>
</section>

<section class="deck deck-3 theme-green" aria-label="Deck in green and yellow">
  <div class="slide grad">
    <div class="photo layer" style="left:96px;width:90px;background:linear-gradient(90deg,rgba(0,0,0,0),rgba(10,20,40,.45))" role="img" aria-label="Photo of a man wearing a VR headset"></div>
    <div class="title-mark">LUMA XR</div>
    <h1 class="title-text">THE FUTURE OF<br>HOSPITALITY<br>TRAINING</h1>
    <div class="badge"></div>
  </div>
  <div class="slide grad">
    <svg class="layer" viewBox="0 0 186 104" preserveAspectRatio="none"><path d="M0 104V88C40 72 70 98 110 78C150 60 158 32 186 40V104Z" fill="#fff"/></svg>
    <div class="mark">LUMA XR</div>
    <h2 class="story-title">Anna’s story…</h2>
    <div class="clip" role="img" aria-label="Newspaper clipping with photo of two men">
      <div class="clip-head">Trainee’s case reviewed after late-night venue incident in Port Ellis</div>
      <div class="clip-by">By staff reporter · updated today</div>
      <div class="clip-photo"></div>
    </div>
  </div>
  <div class="slide grad">
    <svg class="layer" viewBox="0 0 186 104" preserveAspectRatio="none" role="img" aria-label="Photo of a man in a suit"><path d="M0 0H112C96 20 70 30 76 55C82 80 60 94 70 104H0Z" fill="#222"/></svg>
    <div class="mark">LUMA XR</div>
    <div class="problem-label">THE<br>PROBLEM</div>
    <p class="problem-copy">Traditional training does not prepare staff to be</p>
    <p class="job-ready">Job Ready</p>
  </div>
  <div class="slide">
    <div class="layer grad" style="opacity:.6" role="img" aria-label="Photo of a bored student resting on a desk"></div>
    <svg class="layer" viewBox="0 0 186 104" preserveAspectRatio="none"><path d="M186 0H104C126 16 106 40 114 56C122 76 150 86 160 104H186Z" fill="#fff"/></svg>
    <p class="trad-text">Traditional training</p>
  </div>
  <div class="slide grad">
    <svg class="layer" viewBox="0 0 186 104" preserveAspectRatio="none"><path d="M0 0H96C80 16 96 36 86 56C76 76 86 94 80 104H0Z" fill="#fff"/></svg>
    <div class="mark">LUMA XR</div>
    <p class="vr-text">Virtual<br>reality<br>training</p>
    <ul class="ticks">
      <li><svg viewBox="0 0 10 10"><circle cx="5" cy="5" r="5" fill="#fff"/><path d="M2.5 5l1.8 1.8L7.6 3.4" stroke="var(--c1)" stroke-width="1.4" fill="none"/></svg>Retention of knowledge</li>
      <li><svg viewBox="0 0 10 10"><circle cx="5" cy="5" r="5" fill="#fff"/><path d="M2.5 5l1.8 1.8L7.6 3.4" stroke="var(--c1)" stroke-width="1.4" fill="none"/></svg>Real-life experiences</li>
      <li><svg viewBox="0 0 10 10"><circle cx="5" cy="5" r="5" fill="#fff"/><path d="M2.5 5l1.8 1.8L7.6 3.4" stroke="var(--c1)" stroke-width="1.4" fill="none"/></svg>Immersive &amp; engaging</li>
    </ul>
    <div class="photo" style="left:80px;top:56px;width:92px;height:48px;background:linear-gradient(90deg,rgba(20,20,30,.55),rgba(230,230,230,.55));border-radius:20px 20px 0 0" role="img" aria-label="Two people wearing VR headsets"></div>
  </div>
  <div class="slide grad">
    <div class="uniq-strip"><span class="uniq-text">What makes us unique?</span></div>
    <div class="mark">LUMA XR</div>
    <div class="band band-a"></div><div class="band band-b"></div>
    <div class="member" style="left:36px;top:19px"><div class="avatar"></div><div class="m-name">OWEN HALE</div><div class="m-role">Co Founder and CEO</div></div>
    <div class="member" style="left:84px;top:19px"><div class="avatar"></div><div class="m-name">DR LENA MARSH</div><div class="m-role">Learning and Development Strategist</div></div>
    <div class="member" style="left:132px;top:19px"><div class="avatar"></div><div class="m-name">RITA OKAFOR</div><div class="m-role">Co Founder, Education and Content Director</div></div>
    <div class="member" style="left:36px;top:62px"><div class="avatar"></div><div class="m-name">FELIX BRANDT</div><div class="m-role">360 Film and Post-Production Expert</div></div>
    <div class="member" style="left:84px;top:62px"><div class="avatar"></div><div class="m-name">NORA QUILL</div><div class="m-role">Learning Designer</div></div>
    <div class="member" style="left:132px;top:62px"><div class="avatar"></div><div class="m-name">KEN ARATA</div><div class="m-role">Programmer and Game Developer</div></div>
  </div>
  <div class="slide grad">
    <svg class="layer" viewBox="0 0 186 104" preserveAspectRatio="none"><path d="M82 0H186V104H0V86C20 96 30 72 46 70C64 68 70 50 74 40C80 24 70 14 82 0Z" fill="#fff"/></svg>
    <div class="mark">LUMA XR</div>
    <p class="process-title">Our<br>Process</p>
    <svg class="layer" viewBox="0 0 186 104">
      <g transform="rotate(-112 138 53)" fill="none" stroke-width="15">
        <circle cx="138" cy="53" r="38" style="stroke:var(--s1)" stroke-dasharray="28.8 269.8"/>
        <circle cx="138" cy="53" r="38" style="stroke:var(--s1)" stroke-dasharray="0 29.8 28.8 240"/>
        <circle cx="138" cy="53" r="38" style="stroke:var(--s2)" stroke-dasharray="0 59.6 28.8 210"/>
        <circle cx="138" cy="53" r="38" style="stroke:var(--s1)" stroke-dasharray="0 89.4 28.8 180"/>
        <circle cx="138" cy="53" r="38" style="stroke:var(--s3)" stroke-dasharray="0 119.2 28.8 150"/>
        <circle cx="138" cy="53" r="38" style="stroke:var(--s1)" stroke-dasharray="0 149 28.8 120"/>
        <circle cx="138" cy="53" r="38" style="stroke:#5d6c90" stroke-dasharray="0 178.8 28.8 90"/>
        <circle cx="138" cy="53" r="38" style="stroke:var(--s1)" stroke-dasharray="0 208.6 28.8 60"/>
      </g>
      <text class="seg-label" x="125" y="17">Release</text>
      <text class="seg-label" x="151" y="17">Research</text><text class="seg-label" x="151" y="20">topics</text>
      <text class="seg-label" x="172" y="38">Create</text><text class="seg-label" x="172" y="41">Content</text>
      <text class="seg-label" x="171" y="70">Learning</text><text class="seg-label" x="171" y="73">Design</text>
      <text class="seg-label" x="151" y="88">360 Film</text><text class="seg-label" x="151" y="91">Production</text>
      <text class="seg-label" x="123" y="88">360 Post</text><text class="seg-label" x="123" y="91">Production</text>
      <text class="seg-label" x="104" y="67">Interactive</text><text class="seg-label" x="104" y="70">Gaming</text><text class="seg-label" x="104" y="73">Development</text>
      <text class="seg-label" x="104" y="37">Testing</text>
    </svg>
  </div>
  <div class="slide">
    <div class="mark">LUMA XR</div>
    <h2 class="bm-title">Business model</h2>
    <div class="bar bar-1">Partnerships with<br>training providers<span class="bar-icon">&#9679;&#9679;</span></div>
    <div class="bar bar-2"><span class="bar-icon">$</span>Subscription based with new content released monthly</div>
  </div>
  <div class="slide">
    <div class="mark">LUMA XR</div>
    <svg class="layer" viewBox="0 0 186 104">
      <path d="M48 22C70 22 84 14 100 14M66 52H100M48 82C70 82 84 85 100 85" stroke="#111" stroke-width="1.6" fill="none"/>
      <circle cx="48" cy="52" r="30" fill="none" stroke="#111" stroke-width="3"/>
      <circle cx="48" cy="52" r="24" fill="none" style="stroke:var(--ring)" stroke-width="3.5"/>
      <circle cx="48" cy="52" r="18" fill="#fff" stroke="#888" stroke-width="2.5"/>
    </svg>
    <p class="ask-label">Our<br>ask</p>
    <div class="pill pill-intro"><span class="pill-icon">&#10070;</span>Introductions</div>
    <div class="pill pill-fund"><span class="pill-icon">$</span>Funding</div>
    <div class="pill pill-inv"><span class="pill-icon">&#9679;&#9679;</span>Investors</div>
  </div>
  <div class="slide grad">
    <div class="layer" style="background:linear-gradient(90deg,rgba(255,255,255,0),rgba(255,255,255,.18))" role="img" aria-label="Faint photo of a person wearing a VR headset"></div>
    <div class="mark">LUMA XR</div>
    <p class="q-text">Questions<br>?</p>
  </div>
</section>

</body>
</html>
```